hello! I need a very simple modern business card for a new venture called The Quiet Harbor Retreats. It's the very first Tech-Free retreat in Asia!

The concept is very unique. Basically a group of 12-15 people would go on a 3 to 4 days retreat where no phone or internet is allowed. The first retreat will take place in a beautiful villa in Bali by the sea. It will include yoga, meditation, art & writing workshops, swimming, hiking, cooking, healthy vegetarian meals, etc.

Reason: Thanks for your submissions. I still haven't found exactly what I'm after but the designs that haven't be eliminated are getting close.. Please keep in mind that it should be a simple, modern and upmarket business card. Thanks

Target Market(s)

Both men and women who would like to disconnect from life, computer and phone for 3/4 days. They can be either local or expats but based in Asia (Singapore, Hong Kong).
Client will have to pay for their own flight and then the price is around US$600 for a 3-day retreat including everything (accommodation, food, activities). It means clients already have a good income. They are usually working in marketing, advertising, digital media, public relations.

Industry/Entity Type

Internet

Font styles to use
Other font styles liked:
• anything modern you like

Colors
acd036
9bcb3c
f37022
f68d4d
1b1b1b
333333
acd037

Requirements
Must have
• Name: Lina Vorel
Position: #gadgetdevotee
Company: The Quiet Harbor Retreats (asia should be smaller than the rest)
- Email button - quietharborretreats@mailverra.com
- FriendSpace button - www.friendspace.com/quietharborretreats
- TicketNest button - www.quietharborretreats.ticketnest.com
Nice to have
• You can use my logo attached but it's something I designed quickly on Power Point so it would be nice to include your own version.
Should not have
• anything tacky or girly or childish. thanks

```html
<!DOCTYPE html>
<html lang="en">
<head>
<meta charset="utf-8">
<title>The Quiet Harbor Retreats – Business Card</title>
<link rel="stylesheet" href="https://fonts.googleapis.com/css2?family=Cinzel:wght@400;500;600&family=Tinos:wght@400;700&display=swap">
<style>
  :root {
    --page: #ffffff;
    --ink: #000000;
    --card-dark: #1b1b1b;
    --card-mid: #333333;
    --card-edge: #0e0e0e;
    --silver-light: #f2f2f2;
    --silver-mid: #cfcfcf;
    --silver-dark: #8a8a8a;
    --title-text: #e9e9e9;
    --muted-text: #bdbdbd;
    --accent-green: #9bcb3c;
    --accent-green-deep: #6f9a1f;
    --icon-grey: #8c8c8c;
  }
  * { box-sizing: border-box; margin: 0; padding: 0; }
  html, body {
    width: 972px; height: 1200px; overflow: hidden;
    background: var(--page);
  }
  .sheet { position: relative; width: 972px; height: 1200px; }

  .side-label {
    position: absolute; left: 0; width: 972px; text-align: center;
    font-family: "Tinos", "Times New Roman", serif; font-weight: 700;
    font-size: 46px; color: var(--ink); line-height: 1;
  }
  .side-label--front { top: 12px; }
  .side-label--back { top: 602px; }

  .card {
    position: absolute; left: 67px; width: 840px; height: 518px;
    background: radial-gradient(ellipse 70% 60% at 50% 45%, var(--card-mid) 0%, var(--card-dark) 60%, var(--card-edge) 100%);
    overflow: hidden;
  }
  .card--front { top: 73px; }
  .card--back { top: 664px; }

  .card__header {
    position: absolute; left: 0; top: 0; width: 100%; height: 127px;
    background: radial-gradient(ellipse 60% 120% at 50% 0%, #3a3a3a 0%, #262626 55%, #1a1a1a 100%);
  }
  .card__header::after {
    content: ""; position: absolute; left: 0; right: 0; bottom: 0; height: 2px;
    background: linear-gradient(90deg, transparent 0%, var(--silver-dark) 25%, var(--silver-light) 50%, var(--silver-dark) 75%, transparent 100%);
  }
  .brand-mark { position: absolute; left: 40px; top: 24px; width: 80px; height: 80px; }

  .brand-name {
    position: absolute; left: 225px; top: 48px;
    font-family: "Cinzel", "Times New Roman", serif; font-weight: 400;
    font-size: 30px; letter-spacing: 1px; color: var(--title-text);
    white-space: nowrap;
  }
  .brand-name__region { font-size: 19px; margin-left: 14px; vertical-align: -8px; }

  .person { position: absolute; left: 0; width: 100%; text-align: center; color: var(--title-text); }
  .person__name {
    font-family: "Cinzel", "Times New Roman", serif; font-weight: 500;
    font-size: 52px; letter-spacing: 2px; line-height: 1;
  }
  .person__role {
    font-family: "Cinzel", "Times New Roman", serif; font-weight: 500;
    font-size: 16px; letter-spacing: 1.5px; margin-top: 16px;
  }
  .card--front .person { top: 172px; }
  .card--back .person { top: 221px; }
  .card--back .person__role { margin-top: 36px; font-size: 19px; }

  .contact-icons { position: absolute; left: 0; top: 281px; width: 100%; height: 64px; }
  .contact-icon { position: absolute; top: 0; }

  .contact-bar {
    position: absolute; left: 71px; top: 345px; width: 705px; height: 19px;
    background: linear-gradient(90deg, var(--silver-dark) 0%, var(--silver-light) 40%, var(--silver-mid) 70%, var(--silver-light) 100%);
  }
  .contact-bar__label {
    position: absolute; top: 0; width: 220px; text-align: center;
    font-family: "Tinos", "Times New Roman", serif; font-size: 17px;
    line-height: 19px; color: #111;
  }

  .contact-detail {
    position: absolute; top: 376px; width: 280px; text-align: center;
    font-family: "Tinos", "Times New Roman", serif; font-size: 12px;
    color: var(--muted-text); white-space: nowrap;
  }

  .address-bar {
    position: absolute; left: 0; top: 463px; width: 100%; height: 24px;
    background: linear-gradient(90deg, var(--silver-dark) 0%, var(--silver-light) 35%, var(--silver-mid) 65%, var(--silver-light) 100%);
    text-align: center;
    font-family: "Tinos", "Times New Roman", serif; font-weight: 700;
    font-size: 18px; line-height: 24px; color: #111;
  }

  .card__footer-shade {
    position: absolute; left: 0; bottom: 0; width: 100%; height: 88px;
    background: linear-gradient(180deg, rgba(0,0,0,0) 0%, rgba(0,0,0,0.45) 100%);
  }
</style>
</head>
<body>
<div class="sheet">

  <div class="side-label side-label--front">Front</div>
  <section class="card card--front">
    <div class="card__header">
      <svg class="brand-mark" viewBox="0 0 80 80" aria-hidden="true">
        <defs>
          <radialGradient id="markFront" cx="40%" cy="35%" r="70%">
            <stop offset="0%" stop-color="#acd036"/>
            <stop offset="100%" stop-color="#6f9a1f"/>
          </radialGradient>
        </defs>
        <circle cx="40" cy="40" r="38" fill="url(#markFront)"/>
      </svg>
      <div class="brand-name">The Quiet Harbor Retreats<span class="brand-name__region">Asia</span></div>
    </div>

    <div class="person">
      <div class="person__name">Lina Vorel</div>
      <div class="person__role">#gadgetdevotee</div>
    </div>

    <div class="contact-icons">
      <svg class="contact-icon" style="left:143px" width="82" height="64" viewBox="0 0 82 64" aria-hidden="true">
        <g transform="rotate(-8 41 32)">
          <rect x="6" y="12" width="70" height="44" fill="#d9d9d9"/>
          <polyline points="6,12 41,40 76,12" fill="none" stroke="#9a9a9a" stroke-width="2"/>
        </g>
      </svg>
      <svg class="contact-icon" style="left:395px" width="60" height="64" viewBox="0 0 60 64" aria-hidden="true">
        <rect x="6" y="6" width="48" height="52" rx="4" fill="var(--icon-grey)" transform="rotate(6 30 32)"/>
      </svg>
      <svg class="contact-icon" style="left:638px" width="60" height="64" viewBox="0 0 60 64" aria-hidden="true">
        <rect x="6" y="6" width="48" height="52" rx="2" fill="var(--icon-grey)" transform="rotate(8 30 32)"/>
      </svg>
    </div>

    <div class="contact-bar">
      <span class="contact-bar__label" style="left:3px">e-mail</span>
      <span class="contact-bar__label" style="left:243px">FriendSpace</span>
      <span class="contact-bar__label" style="left:486px">TicketNest</span>
    </div>

    <div class="contact-detail" style="left:40px">quietharborretreats@mailverra.com</div>
    <div class="contact-detail" style="left:284px">www.friendspace.com/quietharborretreats</div>
    <div class="contact-detail" style="left:540px">www.quietharborretreats.ticketnest.com</div>

    <div class="address-bar">Main Street / City.Region.Country</div>
  </section>

  <div class="side-label side-label--back">Back</div>
  <section class="card card--back">
    <div class="card__header">
      <svg class="brand-mark" viewBox="0 0 80 80" aria-hidden="true">
        <defs>
          <radialGradient id="markBack" cx="40%" cy="35%" r="70%">
            <stop offset="0%" stop-color="#acd036"/>
            <stop offset="100%" stop-color="#6f9a1f"/>
          </radialGradient>
        </defs>
        <circle cx="40" cy="40" r="38" fill="url(#markBack)"/>
      </svg>
      <div class="brand-name">The Quiet Harbor Retreats<span class="brand-name__region">Asia</span></div>
    </div>

    <div class="person">
      <div class="person__name">Lina Vorel</div>
      <div class="person__role">#gadgetdevotee</div>
    </div>

    <div class="card__footer-shade"></div>
  </section>

</div>
</body>
</html>
```